Need Letterhead Design & Matching Business Card

I have a logo that I love already. But the letterhead is less than appealing and boring. I'd like a design for my letterhead which I will match with business cards. Also, I'd like to have used fonts that are generally available, as my current letterhead uses a font named "SPACE" which nobody has unless they download it...so when a Word version is forwarded, it looks awful on the receiver's screed due to not having the font. That being said, modern is the look we like and are going for.

My business is "Halloran Brightmoor PC" - a law firm specializing in representing people who have suffered catastrophic injuries or death (plane, auto, train crashes etc.).

See attached letterhead, which has all of the pertinent information. My logo is also attached in various formats.

```html
<!DOCTYPE html>
<html lang="en">
<head>
<meta charset="utf-8">
<title>Halloran Brightmoor PC — Letterhead</title>
<link rel="stylesheet" href="https://fonts.googleapis.com/css2?family=Arimo:wght@400&family=Jost:wght@400;500;600&display=swap">
<style>
  :root {
    --backdrop: #b4b0af;
    --paper: #ffffff;
    --ink: #333333;
    --ink-body: #555555;
    --ink-soft: #6f6f6f;
    --rule: #9a9a9a;
    --band: #333333;
  }
  * { box-sizing: border-box; margin: 0; padding: 0; }
  html, body {
    width: 1200px;
    height: 908px;
    overflow: hidden;
    background: var(--backdrop);
  }
  .letterhead {
    position: absolute;
    left: 293px;
    top: 20px;
    width: 613px;
    height: 868px;
    background: var(--paper);
    overflow: hidden;
  }
  .firm-name {
    position: absolute;
    left: 48px;
    top: 106px;
    font-family: "Jost", sans-serif;
    font-weight: 400;
    font-size: 14.5px;
    letter-spacing: 0.6px;
    color: var(--ink);
    text-transform: uppercase;
    white-space: nowrap;
  }
  .contact {
    position: absolute;
    left: 429px;
    top: 46px;
    font-family: "Arimo", sans-serif;
    font-size: 9.4px;
    line-height: 13px;
    color: var(--ink-soft);
    white-space: nowrap;
  }
  .contact-address { margin-bottom: 8px; }
  .contact-line {
    display: flex;
    align-items: center;
    gap: 3px;
    height: 14px;
  }
  .contact-icon { width: 8px; height: 8px; flex: none; }
  .header-rule {
    position: absolute;
    left: 48px;
    top: 125px;
    width: 516px;
    height: 0;
    border-top: 1px solid var(--rule);
  }
  .salutation {
    position: absolute;
    left: 56px;
    top: 267px;
    font-family: "Jost", sans-serif;
    font-weight: 500;
    font-size: 14px;
    color: var(--ink-body);
  }
  .letter-body {
    position: absolute;
    left: 54px;
    top: 306px;
    width: 506px;
    font-family: "Arimo", sans-serif;
    font-size: 9.6px;
    line-height: 12.7px;
    color: var(--ink-body);
  }
  .letter-body p + p { margin-top: 10.8px; }
  .closing {
    position: absolute;
    left: 56px;
    top: 568px;
    font-family: "Jost", sans-serif;
    font-weight: 600;
    font-size: 7.5px;
    color: var(--ink);
  }
  .signature {
    position: absolute;
    left: 55px;
    top: 606px;
    width: 100px;
    height: 28px;
    background: linear-gradient(90deg, #e4e4e4, #d2d2d2);
    border-radius: 3px;
  }
  .footer-swoosh {
    position: absolute;
    left: 0;
    bottom: 0;
    width: 613px;
    height: 86px;
    display: block;
  }
</style>
</head>
<body>
  <main class="letterhead">
    <header>
      <div class="firm-name">Halloran Brightmoor PC</div>
      <address class="contact" style="font-style: normal;">
        <div class="contact-address">4820 Larkspur Ave., suite 600<br>Westhaven, CA 90318</div>
        <div class="contact-line">
          <svg class="contact-icon" viewBox="0 0 10 10" aria-hidden="true"><path d="M2 1 L4 1 L4.6 3 L3.4 3.8 Q4.3 5.8 6.2 6.6 L7 5.4 L9 6 L9 8 Q9 9 8 9 Q1 8.4 1 2 Q1 1 2 1 Z" fill="none" stroke="#444" stroke-width="1"/></svg>
          <span>(555) 014-2290</span>
        </div>
        <div class="contact-line">
          <svg class="contact-icon" viewBox="0 0 10 10" aria-hidden="true"><rect x="0.8" y="2" width="8.4" height="6" fill="none" stroke="#444" stroke-width="1"/><path d="M0.8 2 L5 5.4 L9.2 2" fill="none" stroke="#444" stroke-width="1"/></svg>
          <span>office@halloranbrightmoor.com</span>
        </div>
        <div class="contact-line">
          <svg class="contact-icon" viewBox="0 0 10 10" aria-hidden="true"><circle cx="5" cy="5" r="4.2" fill="none" stroke="#444" stroke-width="1"/><ellipse cx="5" cy="5" rx="1.8" ry="4.2" fill="none" stroke="#444" stroke-width="0.8"/><path d="M0.8 5 H9.2" stroke="#444" stroke-width="0.8"/></svg>
          <span>www.halloranbrightmoor.com</span>
        </div>
      </address>
      <div class="header-rule"></div>
    </header>

    <section class="letter">
      <h1 class="salutation">Dear Mr. Smith,</h1>
      <div class="letter-body">
        <p>Lorem ipsum dolor sit amet, consectetuer adipiscing elit, sed diam nonmmy nibh euismod tincidunt ut laor eet dolore magna aliquam erat volutpat. Ut wisi enim ad minim veniam, quis nostrud exerci tationmcorper suscipit lobortis nisl ut aliquip ex ea commodo consequat. Duis autem vel eum iriure dolor in hendrerit in vulputate velit esse molestie consequat, vel illum dolore eu feugiat</p>
        <p>Rorem ipsum dolor sit amet, consectetuer adipiscing elit, sed diam nonmmy nibh euismod tincidunt ut laor eet dolore magna aliquam erat volutpat. Ut wisi enim ad minim veniam, quis nostrud exerci tationmcorper suscipit lobortis nisl ut aliquip ex ea commodo consequat. Duis autem vel eum iriure dolor in hendrerit in vulputate velit esse molest</p>
        <p>Dorem ipsum dolor sit amet, consectetuer adipiscing elit, sed diam nonmmy nibh euismod tincidunt ut laor eet dolore magna aliquam erat volutpat. Ut wisi enim ad minim veniam, quis nostrud exerci tationmcorper suscipit lobortis nisl ut aliquip ex ea commodo consequat. Duis autem vel eum iriure dolor in hendrerit in suscipit lobortis nisl ut aliquip ex ea commodo consequat. Duis autem vel eum iriure dolor in hendrerit in vulputate velit esse molestie consequat, vel illum</p>
        <p>Sorem ipsum dolor sit amet, consectetuer adipiscing elit, sed diam nonmmy nibh euismod tincidunt ut laor eet dolore magna aliquam erat volutpat. Ut wisi enim ad minim veniam, quis nostrud exerci tationmcorper suscipit lobortis nisl ut aliquip ex ea commodo consequat. Duis autem vel eum iriure dolor in</p>
      </div>
      <p class="closing">Sincerely,</p>
      <div class="signature" role="img" aria-label="Handwritten signature of the sender"></div>
    </section>

    <svg class="footer-swoosh" viewBox="0 1080 846 118" preserveAspectRatio="none" aria-hidden="true">
      <path d="M0 1150 C 220 1182, 520 1182, 846 1124 L846 1198 L0 1198 Z" fill="var(--band)"/>
      <path d="M120 1163 C 420 1186, 660 1160, 846 1114 L846 1122 C 660 1170, 420 1192, 120 1166 Z" fill="var(--paper)"/>
      <path d="M135 1160 C 450 1172, 700 1140, 846 1090 L846 1113 C 660 1158, 420 1178, 135 1162 Z" fill="var(--band)"/>
    </svg>
  </main>
</body>
</html>
```